Weightloss company needs Business Card

We want a business card that is clean and professional, yet portrays that we are a friendly, innovative, and versatile program designed to fit the needs of our clients.
I would like there to be 2 sides, one side having an appointment card, and the other side containing the logo and business information. There can be decorations on both sides. The logo is attached.

Target Market(s)

Men and women 40-60

Industry/Entity Type

Business

Contact Information for Business Card

Font styles to use
Sans Serif

Requirements
Must have
• The logo, space for business information
Nice to have
• The colors in the logo
Should not have
• No pictures of people or food

```html
<!DOCTYPE html>
<html lang="en">
<head>
<meta charset="utf-8">
<title>Brightwell Health – Business Card</title>
<link href="https://fonts.googleapis.com/css2?family=Open+Sans:wght@400;600;700&display=swap" rel="stylesheet">
<style>
  :root{
    --brand-red:#ed1b34;
    --brand-blue:#4dc3e8;
    --ink:#1f1f1f;
    --paper:#ffffff;
    --backdrop:#e6e6e6;
  }
  *{box-sizing:border-box;margin:0;padding:0}
  html,body{width:1200px;height:800px;overflow:hidden}
  body{
    background:var(--backdrop);
    font-family:"Open Sans",Arial,sans-serif;
    position:relative;
  }
  .card{
    position:absolute;
    top:240px;
    width:560px;
    height:320px;
    overflow:hidden;
    box-shadow:0 6px 18px rgba(0,0,0,.18);
  }
  /* Front */
  .card--front{left:26px;background:var(--paper)}
  .brand{
    position:absolute;
    display:flex;align-items:center;gap:10px;
    white-space:nowrap;
  }
  .brand--dark{left:220px;top:40px}
  .brand__name{font-weight:700;font-size:24px;line-height:1;color:var(--brand-red)}
  .brand__mark{width:14px;height:14px;background:var(--brand-blue);flex:none}
  .person{position:absolute;left:112px;top:104px}
  .person__name{color:var(--brand-red);font-weight:600;font-size:17px}
  .person__title{color:var(--ink);font-size:14px;margin-top:2px}
  .person__address{color:var(--ink);font-size:12px;line-height:1.45;margin-top:10px}
  .contact{position:absolute;left:366px;top:190px;color:var(--ink);font-size:12px}
  .contact__web{line-height:1.5;margin-bottom:10px}
  .contact__row{display:flex;line-height:1.55}
  .contact__label{color:var(--brand-red);width:54px}
  .contact__colon{color:var(--brand-red);width:18px}
  .edge-band{position:absolute;left:0;bottom:0;width:100%;height:11px;display:flex}
  .edge-band__blue{width:28%;background:var(--brand-blue)}
  .edge-band__red{flex:1;background:var(--brand-red)}
  /* Back */
  .card--back{left:614px;background:var(--brand-red);color:var(--paper)}
  .appointment__title{
    position:absolute;top:34px;left:0;width:100%;text-align:center;
    font-size:15px;font-weight:600;letter-spacing:.5px;
  }
  .appointment__fields{position:absolute;left:44px;top:74px;right:44px}
  .field{display:flex;align-items:flex-end;font-size:13px;height:30px}
  .field__label{width:60px}
  .field__colon{width:12px}
  .field__line{flex:1;border-bottom:2px dotted var(--paper);margin-bottom:4px}
  .brand--light{left:0;width:100%;justify-content:center;top:226px}
  .brand--light .brand__name{color:var(--paper);font-size:28px}
  .brand--light .brand__mark{background:var(--paper);width:16px;height:16px}
</style>
</head>
<body>
  <section class="card card--front" aria-label="Card front">
    <div class="brand brand--dark">
      <span class="brand__name">Brightwell Health</span>
      <span class="brand__mark"></span>
    </div>
    <div class="person">
      <p class="person__name">John Smith</p>
      <p class="person__title">Managing Director</p>
      <p class="person__address">123 Main Street, One Avenue, NY 12345<br>Address Line 2</p>
    </div>
    <div class="contact">
      <p class="contact__web">info@mail.com<br>www.webaddress.com</p>
      <p class="contact__row"><span class="contact__label">Phone</span><span class="contact__colon">:</span><span>+1 234 567 890</span></p>
      <p class="contact__row"><span class="contact__label">Fax</span><span class="contact__colon">:</span><span>+1 234 567 890</span></p>
      <p class="contact__row"><span class="contact__label">Mobile</span><span class="contact__colon">:</span><span>+1 234 567 890</span></p>
    </div>
    <div class="edge-band"><span class="edge-band__blue"></span><span class="edge-band__red"></span></div>
  </section>

  <section class="card card--back" aria-label="Appointment card">
    <h2 class="appointment__title">APPOINTMENT</h2>
    <div class="appointment__fields">
      <div class="field"><span class="field__label">FOR</span><span class="field__colon">:</span><span class="field__line"></span></div>
      <div class="field"><span class="field__label">DATE</span><span class="field__colon">:</span><span class="field__line"></span></div>
      <div class="field"><span class="field__label">TIME</span><span class="field__colon">:</span><span class="field__line"></span></div>
    </div>
    <div class="brand brand--light">
      <span class="brand__name">Brightwell Health</span>
      <span class="brand__mark"></span>
    </div>
  </section>
</body>
</html>
```